Icons for an Inspections System (codenamed Trevassinor)

We are developing a new system to manage inspections (ie an inspector goes out to a "centre" to perform an inspection which covers say 100 questions/factors).
The home page is adopting Plandora 6 style boxes and we are looking for icons for the top left corner of each box.
All icons are to be white and 40x25 pixels. They are all to be fairly simple in design. I am not looking for anything radically new/different - just something simple and straightforward.
MAIN ITEMS
We need icons for the following main functions:
Centres
Inspectors
Inspections
Self-Inspections
Certificates
Reports
Templates
Categories
Factors
NEW RECORDS
A version of each of the above but with a small asterisk/star shape in one corner to indicate "new". For example: New Centre, New Inspector etc
OTHER ICONS
We also need the same style of icons for the following:
Configuration
Change Password
Sign Out
Other info:
Centres: a centre could be a building or a site where an inspection takes place
Inspector: an inspector is a man or a woman! I was thinking maybe a magnifying glass could be a good icon but I'm open to other ideas
Certificates: when a centre passes an inspection they get a certificate
Templates: these are groups of factors (like questions) to be used on an inspection; they are grouped into categories

Trade associations who are looking to perform inspections on members

```html
<!DOCTYPE html>
<html lang="en">
<head>
<meta charset="utf-8">
<title>Trevassinor — Home Menu Icons</title>
<link rel="stylesheet" href="https://fonts.googleapis.com/css2?family=Source+Sans+3:wght@400&display=swap">
<style>
  :root {
    --page: #ffffff;
    --panel: #6b6b6b;
    --icon: #f4f4f4;
    --label: #555555;
  }
  html, body {
    margin: 0;
    padding: 0;
    width: 1036px;
    height: 1200px;
    overflow: hidden;
    background: var(--page);
  }
  .menu-panel {
    position: absolute;
    left: 0;
    top: 0;
    width: 1036px;
    height: 1200px;
    background: var(--panel);
    border-radius: 34px;
    font-family: "Source Sans 3", "Myriad Pro", sans-serif;
  }
  .menu-item {
    position: absolute;
    width: 300px;
    text-align: center;
  }
  .menu-icon {
    display: block;
    width: 130px;
    height: 125px;
    margin: 0 auto;
  }
  .menu-label {
    margin-top: 14px;
    font-size: 32px;
    line-height: 32px;
    color: var(--label);
  }
  .figure-placeholder {
    display: block;
    margin: 0 auto;
    height: 125px;
    width: 78px;
    background: var(--icon);
    border-radius: 36px 36px 10px 10px;
  }
  .figure-placeholder.small { width: 62px; }
  .col-1 { left: 76px; }
  .col-2 { left: 385px; }
  .col-3 { left: 693px; }
  .row-1 { top: 36px; }
  .row-2 { top: 292px; }
  .row-3 { top: 593px; }
  .row-4 { top: 945px; }
</style>
</head>
<body>
<main class="menu-panel">

  <div class="menu-item col-1 row-1">
    <svg class="menu-icon" viewBox="0 0 120 120" aria-hidden="true">
      <g fill="var(--icon)">
        <rect x="62" y="6" width="34" height="106"/>
        <rect x="38" y="28" width="22" height="84"/>
        <rect x="16" y="52" width="20" height="60"/>
        <rect x="8" y="110" width="104" height="6"/>
      </g>
      <g stroke="var(--panel)" stroke-width="3">
        <line x1="68" y1="22" x2="68" y2="108"/><line x1="76" y1="22" x2="76" y2="108"/>
        <line x1="84" y1="22" x2="84" y2="108"/><line x1="92" y1="22" x2="92" y2="108"/>
        <line x1="38" y1="50" x2="60" y2="50"/><line x1="38" y1="66" x2="60" y2="66"/>
        <line x1="38" y1="82" x2="60" y2="82"/><line x1="38" y1="98" x2="60" y2="98"/>
        <line x1="16" y1="70" x2="36" y2="70"/><line x1="16" y1="88" x2="36" y2="88"/>
      </g>
    </svg>
    <div class="menu-label">Centres</div>
  </div>

  <div class="menu-item col-2 row-1">
    <div class="figure-placeholder" role="img" aria-label="Inspector figure icon"></div>
    <div class="menu-label">Inspectors</div>
  </div>

  <div class="menu-item col-3 row-1">
    <svg class="menu-icon" viewBox="0 0 120 120" aria-hidden="true">
      <rect x="28" y="16" width="62" height="94" rx="4" fill="none" stroke="var(--icon)" stroke-width="7"/>
      <rect x="44" y="6" width="30" height="18" rx="3" fill="var(--icon)"/>
      <g fill="none" stroke="var(--icon)" stroke-width="3">
        <rect x="40" y="38" width="10" height="10"/><rect x="40" y="58" width="10" height="10"/><rect x="40" y="78" width="10" height="10"/>
      </g>
      <g stroke="var(--icon)" stroke-width="4">
        <line x1="56" y1="43" x2="74" y2="43"/><line x1="56" y1="63" x2="66" y2="63"/>
      </g>
      <circle cx="84" cy="88" r="20" fill="var(--icon)" stroke="var(--panel)" stroke-width="4"/>
      <path d="M74 88 L81 95 L94 81" fill="none" stroke="var(--panel)" stroke-width="6"/>
    </svg>
    <div class="menu-label">Inspections</div>
  </div>

  <div class="menu-item col-1 row-2">
    <div class="figure-placeholder small" role="img" aria-label="Self-inspection figure with arrows icon"></div>
    <div class="menu-label">Self-Inspections</div>
  </div>

  <div class="menu-item col-2 row-2">
    <svg class="menu-icon" viewBox="0 0 120 120" aria-hidden="true">
      <rect x="30" y="6" width="60" height="106" fill="none" stroke="var(--icon)" stroke-width="6"/>
      <path d="M58 84 L52 106 L60 100 L66 108 L70 84 Z" fill="var(--icon)"/>
      <circle cx="64" cy="76" r="12" fill="var(--icon)"/>
      <circle cx="64" cy="76" r="5" fill="var(--panel)"/>
    </svg>
    <div class="menu-label">Certificates</div>
  </div>

  <div class="menu-item col-3 row-2">
    <svg class="menu-icon" viewBox="0 0 120 120" aria-hidden="true">
      <g fill="var(--icon)" stroke="var(--panel)" stroke-width="3">
        <rect x="44" y="8" width="52" height="80"/>
        <rect x="36" y="16" width="52" height="80"/>
        <rect x="28" y="24" width="52" height="88"/>
      </g>
      <g stroke="var(--panel)" stroke-width="3">
        <line x1="36" y1="38" x2="72" y2="38"/><line x1="36" y1="46" x2="72" y2="46"/>
        <line x1="36" y1="54" x2="72" y2="54"/><line x1="36" y1="62" x2="72" y2="62"/>
        <line x1="36" y1="70" x2="72" y2="70"/><line x1="36" y1="78" x2="72" y2="78"/>
        <line x1="36" y1="86" x2="72" y2="86"/><line x1="36" y1="94" x2="72" y2="94"/>
      </g>
    </svg>
    <div class="menu-label">Reports</div>
  </div>

  <div class="menu-item col-1 row-3">
    <svg class="menu-icon" viewBox="0 0 120 120" aria-hidden="true">
      <path d="M28 8 H92 V98 L80 110 H28 Z" fill="none" stroke="var(--icon)" stroke-width="7"/>
      <rect x="44" y="34" width="34" height="34" fill="var(--icon)"/>
      <polygon points="61,39 64.5,47 73,47.5 66.5,53 68.5,61.5 61,57 53.5,61.5 55.5,53 49,47.5 57.5,47" fill="var(--panel)"/>
    </svg>
    <div class="menu-label">Templates</div>
  </div>

  <div class="menu-item col-2 row-3">
    <svg class="menu-icon" viewBox="0 0 120 120" aria-hidden="true">
      <rect x="40" y="8" width="40" height="26" rx="4" fill="var(--icon)"/>
      <g fill="none" stroke="var(--icon)" stroke-width="4">
        <path d="M60 34 V56 M20 76 V56 H100 V76 M60 56 V76"/>
      </g>
      <rect x="4" y="76" width="32" height="22" rx="4" fill="var(--icon)"/>
      <rect x="44" y="76" width="32" height="22" rx="4" fill="var(--icon)"/>
      <rect x="84" y="76" width="32" height="22" rx="4" fill="var(--icon)"/>
      <g stroke="var(--panel)" stroke-width="3">
        <line x1="50" y1="17" x2="70" y2="17"/><line x1="50" y1="25" x2="70" y2="25"/>
        <line x1="12" y1="87" x2="28" y2="87"/><line x1="52" y1="87" x2="68" y2="87"/><line x1="92" y1="87" x2="108" y2="87"/>
      </g>
    </svg>
    <div class="menu-label">Categories</div>
  </div>

  <div class="menu-item col-3 row-3">
    <svg class="menu-icon" viewBox="0 0 120 120" aria-hidden="true">
      <g fill="var(--icon)">
        <rect x="2" y="72" width="10" height="38"/>
        <rect x="15" y="50" width="10" height="60"/>
        <rect x="28" y="28" width="10" height="82"/>
        <path d="M76 70 L76 32 A38 38 0 1 0 112 78 Z"/>
        <path d="M82 64 L82 26 A38 38 0 0 1 118 72 Z"/>
      </g>
    </svg>
    <div class="menu-label">Factors</div>
  </div>

  <div class="menu-item col-1 row-4">
    <svg class="menu-icon" viewBox="0 0 120 120" aria-hidden="true">
      <circle cx="80" cy="46" r="24" fill="none" stroke="var(--icon)" stroke-width="10" stroke-dasharray="8 7"/>
      <circle cx="80" cy="46" r="20" fill="var(--icon)"/>
      <circle cx="80" cy="46" r="8" fill="var(--panel)"/>
      <circle cx="30" cy="82" r="19" fill="none" stroke="var(--icon)" stroke-width="9" stroke-dasharray="7 6"/>
      <circle cx="30" cy="82" r="16" fill="var(--icon)"/>
      <circle cx="30" cy="82" r="6" fill="var(--panel)"/>
    </svg>
    <div class="menu-label">Configuration</div>
  </div>

  <div class="menu-item col-2 row-4">
    <svg class="menu-icon" viewBox="0 0 120 120" aria-hidden="true">
      <path d="M30 62 V30 A18 18 0 0 1 66 30 V38" fill="none" stroke="var(--icon)" stroke-width="10"/>
      <rect x="42" y="54" width="62" height="58" fill="var(--icon)"/>
      <g fill="var(--panel)">
        <rect x="42" y="64" width="6" height="4"/><rect x="42" y="76" width="6" height="4"/>
        <rect x="42" y="88" width="6" height="4"/><rect x="42" y="100" width="6" height="4"/>
      </g>
    </svg>
    <div class="menu-label">Change<br>Password</div>
  </div>

  <div class="menu-item col-3 row-4">
    <svg class="menu-icon" viewBox="0 0 120 120" aria-hidden="true">
      <path d="M42 34 A40 40 0 1 0 78 34" fill="none" stroke="var(--icon)" stroke-width="10"/>
      <line x1="60" y1="6" x2="60" y2="62" stroke="var(--icon)" stroke-width="10"/>
    </svg>
    <div class="menu-label">Sign Out</div>
  </div>

</main>
</body>
</html>
```